Meridian Harvest Partners- Web & Business card design for a new business within the Ag Sector

HELLO!!!!

We need your help in relation to web design (business cards and stationary if possible!) for a new company based in NSW, Australia.

The name of the business is: Meridian Harvest Partners (MHP). I have quickly mocked a webpage just to give you an idea of what we are looking for.... http://corvelland7.sitebuilderdemo.net/http

MHP is a strategic advisory, investment manager and problem solver within the Australian Agricultural sector.

Our Mission:

We are here to provide solutions to ALL of our Clients needs and desires within the Agricultural space.

Our Team:

Our team has worked with some of the largest & oldest Agricultural companies in Australia

We provide our Clients with a unique blend of the best Corporate as well as Operational experience that the Industry has to offer.

Client-driven Services Approach:

MHP offers a tailored service in order to meet the objectives and outcomes for each and every client.

Some of our services include:

- Food Security / Supply

- Procurement strategies within and across agricultural supply-chains

- Strategic Agribusiness advice for both Australian and Chinese based agricultural enterprises

- M&A / Due Diligence

- Corporate governance & risk management strategies.

I have attached a copy of our capability statement for background reading.

We look forward to receiving your designs!!!!!!!
Updates

Target Market(s)

Corporate, Family Offices, Food Services & Supermarkets - that are looking to obtain products within the agricultural space. Whether it be boxed beef, grain, live animals, advice - ie M&A, Due diligence - just think anything "Agricultural" and we can provide a solution

Industry/Entity Type

Agriculture

Contact Information for Business Card

See below

With respect to the business cards:

There are 2 Managing Directors:

1. Marcus Tilden
Managing Director
E: marcus.tilden@meridianharvestpartners.example
M: +61 400 913 642
W: www.meridianharvestpartners.example

2. Rachel Dunmore
Managing Director
E: rachel.dunmore@meridianharvestpartners.example
M: +61 400 276 418

Please see attached 2 * Files named Brenwick that outline a layout of business card that I like

Coding

Coded - Design and coding required

Number of Pages Required

5+ page

Font styles to use
Sans Serif
Other font styles liked:
• Calibri

Requirements
Must have
• I like the look of this website: http://fieldvoxtrend.example/
• And I like the themes in the website that I have mocked up: http://corvelland7.sitebuilderdemo.net/http
• The wow factor, with a professional twist.
• With respect to the website - would like it to follow the flow of the capability statement - ie with a home page, and the four additional pages:
• ABOUT US
• OUR SERVICES
• OUR TEAM
• CONTACT DETAILS
• The powerpoint presentation that I have attached is simply there for content direction - not design direction.
• As a result, am looking for web design / business card that stands out - is corporate - yet still agricultural feel.
• "capability statement" simply refers to a document that outlines our capabilities - and does not form part of the business name.
• A black angus cow, or a stalk of wheat - greens and yellows may better represent the Ag space.
• This s a draft mock-up of a web-site I created with one of those free web-page makers... This should give you a feel - crisp - whites - yet agricultural tones to highlight
• The attachments below should be used as inspiration - and don't need to be the actual shots used.

```html
<!DOCTYPE html>
<html lang="en">
<head>
<meta charset="utf-8">
<title>Meridian Harvest Partners</title>
<link rel="stylesheet" href="https://fonts.googleapis.com/css2?family=PT+Sans:wght@400;700&family=PT+Serif:wght@400;700&display=swap">
<style>
  :root {
    --page-bg: #f2f2f2;
    --panel-bg: #ffffff;
    --ink: #111111;
    --body-text: #444444;
    --nav-bg: #3d3d3d;
    --nav-text: #ffffff;
    --label-bg: #000000;
    --button-border: #666666;
    --icon-bg: #3a3a3a;
    --icon-line: #ffffff;
  }
  * { box-sizing: border-box; margin: 0; padding: 0; }
  html, body { width: 1032px; height: 1200px; overflow: hidden; }
  body { background: var(--page-bg); position: relative; font-family: "PT Sans", sans-serif; color: var(--body-text); }
  .page { position: absolute; left: 133px; top: 0; width: 766px; height: 1133px; background: var(--panel-bg); }

  .brand { position: absolute; left: 52px; top: 44px; font-family: "PT Serif", serif; font-weight: 700; font-size: 25px; line-height: 30px; color: var(--ink); white-space: nowrap; }
  .social { position: absolute; left: 607px; top: 56px; display: flex; gap: 5px; }
  .social-icon { width: 32px; height: 24px; background: var(--icon-bg); display: flex; align-items: center; justify-content: center; }

  .main-nav { position: absolute; left: 52px; top: 127px; width: 662px; height: 33px; background: var(--nav-bg); }
  .main-nav a { position: absolute; top: 7px; color: var(--nav-text); text-decoration: none; font-size: 16px; line-height: 18px; transform: translateX(-50%); white-space: nowrap; }
  .main-nav a.active { border-bottom: 1px solid var(--nav-text); padding-bottom: 3px; }

  .hero { position: absolute; left: 52px; top: 160px; width: 662px; height: 341px; overflow: visible;
    background:
      radial-gradient(ellipse 30% 22% at 30% 50%, rgba(20,20,20,0.9), rgba(20,20,20,0) 100%),
      radial-gradient(ellipse 28% 24% at 65% 46%, rgba(22,22,22,0.9), rgba(22,22,22,0) 100%),
      radial-gradient(ellipse 14% 30% at 95% 45%, rgba(26,26,26,0.85), rgba(26,26,26,0) 100%),
      linear-gradient(180deg, #4a6a34 0%, #3c5a2a 14%, #6f8f4a 24%, #8aa85a 32%, #7e9c50 55%, #9fbd62 70%, #b6cf7c 85%, #a9c46c 100%); }
  .hero-arrow { position: absolute; top: 127px; width: 20px; height: 86px; background: #ffffff; }
  .hero-arrow.prev { left: -6px; }
  .hero-arrow.next { right: -6px; }
  .hero-arrow svg { position: absolute; left: 3px; top: 25px; }

  .cards { position: absolute; left: 54px; top: 563px; }
  .card { position: absolute; width: 155px; top: 0; text-align: center; }
  .card-photo { height: 161px; border: 1px solid #d6d6d6; }
  .card-label { height: 29px; background: var(--label-bg); color: #fff; font-family: "PT Serif", serif; font-size: 16px; line-height: 29px; }
  .card-text { margin-top: 6px; font-size: 13px; line-height: 22px; white-space: nowrap; }
  .card-button { display: block; margin-top: 6px; height: 29px; border: 1px solid var(--button-border); color: var(--ink); font-weight: 700; font-size: 13px; line-height: 27px; text-decoration: none; }

  .intro { position: absolute; left: 0; top: 933px; width: 766px; text-align: center; }
  .intro h1 { font-family: "PT Serif", serif; font-weight: 400; font-size: 23px; color: #222; }
  .intro p { width: 570px; margin: 22px auto 0; font-size: 13px; line-height: 22px; }
</style>
</head>
<body>
<div class="page">
  <div class="brand">Meridian Harvest Partners</div>
  <div class="social" aria-label="Social links">
    <span class="social-icon" aria-label="Message"><svg width="16" height="14" viewBox="0 0 16 14"><path d="M2 1h12a1 1 0 0 1 1 1v7a1 1 0 0 1-1 1H7l-3 3v-3H2a1 1 0 0 1-1-1V2a1 1 0 0 1 1-1z" fill="none" stroke="#fff" stroke-width="1.4"/></svg></span>
    <span class="social-icon" aria-label="Email"><svg width="16" height="12" viewBox="0 0 16 12"><rect x="1" y="1" width="14" height="10" fill="none" stroke="#fff" stroke-width="1.4"/><polyline points="1,1 8,7 15,1" fill="none" stroke="#fff" stroke-width="1.4"/></svg></span>
    <span class="social-icon" aria-label="Share"><svg width="14" height="14" viewBox="0 0 14 14"><circle cx="3" cy="7" r="2" fill="#fff"/><circle cx="11" cy="2.5" r="2" fill="#fff"/><circle cx="11" cy="11.5" r="2" fill="#fff"/><line x1="3" y1="7" x2="11" y2="2.5" stroke="#fff" stroke-width="1.3"/><line x1="3" y1="7" x2="11" y2="11.5" stroke="#fff" stroke-width="1.3"/></svg></span>
  </div>

  <nav class="main-nav">
    <a class="active" href="#" style="left:50px">HOME</a>
    <a href="#" style="left:155px">ABOUT US</a>
    <a href="#" style="left:288px">OUR SERVICES</a>
    <a href="#" style="left:422px">OUR TEAM</a>
    <a href="#" style="left:572px">CONTACT DETAIL</a>
  </nav>

  <div class="hero" role="img" aria-label="Slideshow photo: black angus cattle grazing in a green paddock">
    <div class="hero-arrow prev"><svg width="14" height="36" viewBox="0 0 14 36"><polyline points="12,2 2,18 12,34" fill="none" stroke="#222" stroke-width="1.6"/></svg></div>
    <div class="hero-arrow next"><svg width="14" height="36" viewBox="0 0 14 36"><polyline points="2,2 12,18 2,34" fill="none" stroke="#222" stroke-width="1.6"/></svg></div>
  </div>

  <div class="cards">
    <div class="card" style="left:0">
      <div class="card-photo" role="img" aria-label="Golden wheat ears" style="background:radial-gradient(ellipse 60% 70% at 40% 55%, #e0a83e, rgba(224,168,62,0) 80%), linear-gradient(135deg,#f6e4b4,#ecc77a 60%,#f3ddb0)"></div>
      <div class="card-label">About US</div>
      <p class="card-text">Lorem Ipsum is simply<br>dummy text of the printing<br>and typesetting industry.<br>Lorem Ipsum.</p>
      <a class="card-button" href="#">Read more</a>
    </div>
    <div class="card" style="left:168px">
      <div class="card-photo" role="img" aria-label="Combine harvester working a grain field" style="background:radial-gradient(ellipse 35% 45% at 80% 80%, #4f9a4a, rgba(79,154,74,0) 90%), linear-gradient(170deg,#dfe8ee 0%,#b8c4c8 22%,#5d6358 40%,#8e6f4e 65%,#a88560 100%)"></div>
      <div class="card-label">OUR SERVICES</div>
      <p class="card-text">Lorem Ipsum is simply<br>dummy text of the printing<br>and typesetting industry.<br>Lorem Ipsum.</p>
      <a class="card-button" href="#">Read more</a>
    </div>
    <div class="card" style="left:336px">
      <div class="card-photo" role="img" aria-label="Two advisers reviewing a tablet in a farm field" style="background:radial-gradient(ellipse 40% 60% at 70% 60%, #eef0ee, rgba(238,240,238,0) 85%), radial-gradient(ellipse 30% 60% at 22% 65%, #6f7e86, rgba(111,126,134,0) 85%), linear-gradient(180deg,#e6eef0 0%,#a9c98a 30%,#74a84e 60%,#8fa078 100%)"></div>
      <div class="card-label">OUR TEAM</div>
      <p class="card-text">Lorem Ipsum is simply<br>dummy text of the printing<br>and typesetting industry.<br>Lorem Ipsum.</p>
      <a class="card-button" href="#">Read more</a>
    </div>
    <div class="card" style="left:504px">
      <div class="card-photo" role="img" aria-label="Support staff member with a headset" style="background:radial-gradient(ellipse 45% 55% at 52% 45%, #e9cba8, rgba(233,203,168,0) 85%), linear-gradient(180deg,#ffffff 0%,#f6f1ea 55%,#d9dbe2 100%)"></div>
      <div class="card-label">CONTACT</div>
      <p class="card-text">Lorem Ipsum is simply<br>dummy text of the printing<br>and typesetting industry.<br>Lorem Ipsum.</p>
      <a class="card-button" href="#">Read more</a>
    </div>
  </div>

  <section class="intro">
    <h1>Meridian Harvest Partners</h1>
    <p>Contrary to popular belief, Lorem Ipsum is not simply random text. It has roots in a piece of classical Latin literature from 45 BC, making it over 2000 years old. Edmund Varley, looked up one of the more obscure Latin words, consectetur, from a Lorem Ipsum passage, and going through the cites of the word in classical literature,</p>
  </section>
</div>
</body>
</html>
```